Tri-fold brochue, business card, and stationary design.

Tri-fold brochure: We are looking to get a tri-fold brochure template created so we can add our content on each side of the brochure and then leave these with prospective clients during sales calls.Business card: We would like the business card to have employee name, phone number, and email address on the card. We are open to rounded corners as well.We just redid our website and we'd like all designs to be complementary to our new "Look and feel" of our website.

Contact Information for Business Card

We would like the business card to have employee name, phone number, and email address on the card. We are open to rounded corners as well.

We just redid our website and we'd like all designs to be complementary to our new "Look and feel" of our website.

```html
<!DOCTYPE html>
<html lang="en">
<head>
<meta charset="utf-8">
<title>Tidewell Networks – Tri-fold Brochure</title>
<link href="https://fonts.googleapis.com/css2?family=Open+Sans:wght@300;400;600;700&display=swap" rel="stylesheet">
<style>
  :root{
    --page-bg:#ececec;
    --brand-blue:#2196d9;
    --brand-blue-dark:#1b7cc9;
    --brand-blue-light:#35aee8;
    --cyan:#18b0e6;
    --panel-light:#f5f7f9;
    --charcoal:#4d4e50;
    --ink:#3a3a3a;
    --body-ink:#4a4a4a;
    --accent-green:#7cb92a;
    --white:#ffffff;
  }
  *{box-sizing:border-box;margin:0;padding:0}
  html,body{width:810px;height:1200px;overflow:hidden;background:var(--page-bg);font-family:"Open Sans",Arial,sans-serif}
  .canvas{position:relative;width:810px;height:1200px}
  .spread{position:absolute;left:47px;width:716px;height:516px;overflow:hidden;background:var(--white);box-shadow:0 10px 22px rgba(0,0,0,.18)}
  .spread--outside{top:40px}
  .spread--inside{top:632px}
  .spread-art{position:absolute;left:0;top:0}
  .txt{position:absolute}

  /* outside spread */
  .flap-title{left:0;top:94px;width:246px;text-align:center;color:var(--white);font-size:14px;font-weight:400;line-height:19px;letter-spacing:.2px}
  .feature{font-size:8.6px;line-height:11px;color:var(--white);width:112px}
  .intro-heading{left:246px;top:100px;width:230px;text-align:center;font-size:20px;font-weight:600;color:var(--ink)}
  .intro-copy{left:266px;top:134px;width:190px;font-size:10.6px;line-height:14.9px;color:var(--body-ink);text-align:justify;hyphens:auto}
  .contact-label{left:274px;top:348px;font-size:11.5px;font-weight:600;color:var(--white);letter-spacing:.3px}
  .contact-list{left:288px;top:372px;list-style:none}
  .contact-list li{display:flex;align-items:center;height:21px;font-size:11.5px;color:var(--white)}
  .contact-list svg{width:14px;height:14px;margin-right:12px;flex:none}
  .mini-brand{left:246px;top:462px;width:230px;display:flex;justify-content:center;align-items:center;gap:5px;font-size:7px;font-weight:600;color:var(--white)}
  .mini-brand .dot{width:11px;height:11px;border-radius:50%;background:var(--white)}
  .brand{left:476px;top:70px;width:240px;display:flex;justify-content:center;align-items:center;gap:8px;color:var(--brand-blue);font-weight:600}
  .brand .dot{width:28px;height:28px;border-radius:50%;background:var(--brand-blue)}
  .brand-name{font-size:16px;line-height:17px}
  .brand-name span{display:block;font-size:8px;letter-spacing:3px;line-height:10px}
  .cover-headline{left:476px;top:118px;width:240px;text-align:center;font-size:19px;font-weight:700;line-height:23px;color:var(--brand-blue)}
  .cover-url{left:476px;top:220px;width:240px;text-align:center;font-size:9.5px;font-weight:700;color:var(--brand-blue)}

  /* inside spread */
  .inside-heading{left:32px;top:26px;font-size:24px;font-weight:700;line-height:28px;color:var(--white)}
  .circle-quote{left:99px;top:228px;width:184px;text-align:center;font-size:14px;font-weight:600;line-height:18px;color:var(--white)}
  .copy-small{font-size:8.5px;line-height:11.8px;color:var(--body-ink);text-align:justify;hyphens:auto}
  .copy-left{left:33px;top:380px;width:198px;font-size:9.4px;line-height:12px}
  .copy-a{left:266px;top:32px;width:198px}
  .copy-b{left:322px;top:172px;width:142px}
  .copy-c{left:266px;top:408px;width:198px}
  .steps{left:511px;top:42px;list-style:none;width:196px}
  .steps li{display:flex;align-items:flex-start;height:42px;color:var(--white)}
  .steps .num{font-size:18px;font-weight:300;width:20px;flex:none;line-height:20px}
  .steps h3{font-size:10px;font-weight:400;line-height:12px}
  .steps p{font-size:5.6px;line-height:7.2px;opacity:.9}
</style>
</head>
<body>
<div class="canvas">

  <!-- Outside spread -->
  <section class="spread spread--outside">
    <svg class="spread-art" width="716" height="516" viewBox="0 0 716 516">
      <defs>
        <linearGradient id="flapBlue" x1="0" y1="0" x2="0" y2="1">
          <stop offset="0" stop-color="#1d80cc"/><stop offset="1" stop-color="#2ba2e6"/>
        </linearGradient>
        <radialGradient id="grassTone" cx=".45" cy=".45" r=".6">
          <stop offset="0" stop-color="#eef0ec"/><stop offset=".6" stop-color="#c9d0c0"/><stop offset="1" stop-color="#8fa57a"/>
        </radialGradient>
      </defs>
      <rect x="0" y="0" width="246" height="516" fill="url(#flapBlue)"/>
      <rect x="246" y="0" width="230" height="516" fill="#fff"/>
      <rect x="476" y="0" width="240" height="516" fill="#f5f7f9"/>
      <rect x="246" y="338" width="230" height="178" fill="#4d4e50"/>
      <circle cx="472" cy="42" r="62" fill="#fff"/>
      <circle cx="472" cy="42" r="44" fill="#38a9e1"/>
      <circle cx="614" cy="416" r="128" fill="#fff"/>
      <g role="img" aria-label="Photo of dew-covered grass blades and spider web in morning mist">
        <circle cx="614" cy="416" r="116" fill="url(#grassTone)"/>
      </g>
      <circle cx="542" cy="292" r="46" fill="#fff"/>
      <circle cx="542" cy="292" r="30" fill="#2a9bdc"/>

      <g fill="#fff">
        <circle cx="62" cy="182" r="30"/><circle cx="193" cy="250" r="30"/>
        <circle cx="62" cy="324" r="30"/><circle cx="193" cy="394" r="30"/>
      </g>
      <g class="icon-gear">
        <circle cx="62" cy="182" r="13" fill="none" stroke="#7cb92a" stroke-width="6" stroke-dasharray="5 5.2"/>
        <circle cx="62" cy="182" r="10" fill="#7cb92a"/>
        <circle cx="62" cy="182" r="4" fill="#fff"/>
      </g>
      <g class="icon-globe" fill="none" stroke="#7cb92a" stroke-width="2">
        <circle cx="193" cy="250" r="15"/>
        <ellipse cx="193" cy="250" rx="7" ry="15"/>
        <line x1="178" y1="250" x2="208" y2="250"/>
        <line x1="193" y1="235" x2="193" y2="265"/>
        <path d="M180 242h26M180 258h26"/>
      </g>
      <path class="icon-heart" d="M62 337 C44 324 44 310 53 308 C58 307 61 310 62 313 C63 310 66 307 71 308 C80 310 80 324 62 337Z" fill="#7cb92a"/>
      <g class="icon-sun">
        <circle cx="193" cy="394" r="16" fill="none" stroke="#7cb92a" stroke-width="6" stroke-dasharray="3 4.4"/>
        <circle cx="193" cy="394" r="9" fill="#7cb92a"/>
      </g>
    </svg>

    <h2 class="txt flap-title">LOREM IPSUM IS<br>SIMPL TEXT</h2>
    <p class="txt feature" style="left:130px;top:160px">Lorem Ipsum is simply dummy text of the printing and typesetting industry.</p>
    <p class="txt feature" style="left:32px;top:230px;width:125px">Lorem Ipsum is simply dummy text of the printing and typesetting industry.</p>
    <p class="txt feature" style="left:130px;top:302px">Lorem Ipsum is simply dummy text of the printing and typesetting industry.</p>
    <p class="txt feature" style="left:32px;top:374px;width:125px">Lorem Ipsum is simply dummy text of the printing and typesetting industry.</p>

    <h2 class="txt intro-heading">Lorem ipsum</h2>
    <p class="txt intro-copy">Lorem ipsum dolor sit amet, consectetuer adipiscing elit, sed diam nonummy nibh euismod tincidunt ut laoreet dolore magna aliquam erat volutpat. Ut wisi enim ad minim veniam, quis nostrud exerci tation ullamcorper suscipit lobortis nisl ut aliquip ex ea commodo consequat. Duis autem vel eum iriure dolor in hendrerit in vulputate velit</p>

    <h3 class="txt contact-label">CONTACT</h3>
    <ul class="txt contact-list">
      <li><svg viewBox="0 0 16 16"><path d="M3 1l3 3-2 2c1 2 3 4 5 5l2-2 3 3-2 3C7 14 2 9 1 3z" fill="#fff"/></svg>65.4410.2286</li>
      <li><svg viewBox="0 0 16 16"><rect x="1" y="3" width="14" height="10" fill="none" stroke="#fff" stroke-width="1.5"/><path d="M1 3l7 6 7-6" fill="none" stroke="#fff" stroke-width="1.5"/></svg>hello@tidewellmail.com</li>
      <li><svg viewBox="0 0 16 16" fill="none" stroke="#fff" stroke-width="1.3"><circle cx="8" cy="8" r="6.5"/><ellipse cx="8" cy="8" rx="3" ry="6.5"/><path d="M1.5 8h13M2.5 5h11M2.5 11h11"/></svg>www.tidewell.net</li>
      <li><svg viewBox="0 0 16 16"><path d="M8 15C4 10 3 8 3 6a5 5 0 0 1 10 0c0 2-1 4-5 9z" fill="#fff"/><circle cx="8" cy="6" r="2" fill="#4d4e50"/></svg>harbor lane 42, CA, USA</li>
    </ul>
    <div class="txt mini-brand"><span class="dot"></span>Tidewell</div>

    <div class="txt brand"><span class="dot"></span><div class="brand-name">Tidewell<span>Networks</span></div></div>
    <h1 class="txt cover-headline">IT SUPPORT<br>GIVING YOU THE<br>BLUES?</h1>
    <p class="txt cover-url">www.tidewellnetworks.com</p>
  </section>

  <!-- Inside spread -->
  <section class="spread spread--inside">
    <svg class="spread-art" width="716" height="516" viewBox="0 0 716 516">
      <defs>
        <linearGradient id="panelBlue" x1="0" y1="0" x2="0" y2="1">
          <stop offset="0" stop-color="#1f88d2"/><stop offset="1" stop-color="#2ba3e6"/>
        </linearGradient>
        <radialGradient id="lockTone" cx=".4" cy=".45" r=".65">
          <stop offset="0" stop-color="#3f8fd6"/><stop offset=".55" stop-color="#1a4d92"/><stop offset="1" stop-color="#0b1d45"/>
        </radialGradient>
      </defs>
      <rect x="0" y="0" width="246" height="516" fill="url(#panelBlue)"/>
      <rect x="246" y="0" width="230" height="516" fill="#fff"/>
      <rect x="476" y="0" width="240" height="516" fill="url(#panelBlue)"/>

      <circle cx="191" cy="256" r="140" fill="#fff"/>
      <path d="M0 516 L0 392 Q0 346 60 336 L246 336 L246 516 Z" fill="#fff"/>
      <circle cx="191" cy="256" r="114" fill="#18b0e6" opacity=".94"/>

      <circle cx="601" cy="402" r="150" fill="#fff"/>
      <rect x="476" y="402" width="240" height="114" fill="#fff"/>
      <circle cx="531" cy="282" r="38" fill="#fff"/>
      <circle cx="531" cy="282" r="26" fill="#333436"/>
      <g role="img" aria-label="Photo of a glowing digital padlock over binary code">
        <circle cx="604" cy="408" r="118" fill="url(#lockTone)"/>
      </g>
      <g role="img" aria-label="World map with connection points">
        <rect x="301" y="318" width="164" height="82" rx="6" fill="#2aa3e3" opacity=".85"/>
      </g>
    </svg>

    <h2 class="txt inside-heading">Lorem ipsum<br>dolor sit amet,</h2>
    <p class="txt circle-quote">Lorem ipsum dolor sit amet, consectetuer adipiscing elit, sed diam nonummy nibh euismod</p>
    <p class="txt copy-small copy-left">Lorem ipsum dolor sit amet, consectetuer adipiscing elit, sed diam nonummy nibh euismod tincidunt ut laoreet dolore magna aliquam erat volutpat. Ut wisi enim ad minim veniam, quis nostrud exerci tation ullamcorper suscipit lobortis nisl ut aliquip ex ea commodo consequat. Duis autem vel eum iriure dolor in hendrerit in vulputate velit esse molestie consequat, vel illum dolore eu feugiat</p>

    <p class="txt copy-small copy-a">Lorem ipsum dolor sit amet, consectetuer adipiscing elit, sed diam nonummy nibh euismod tincidunt ut laoreet dolore magna aliquam erat volutpat. Ut wisi enim ad minim veniam, quis nostrud exerci tation ullamcorper suscipit lobortis nisl ut aliquip ex ea commodo consequat. Duis autem vel eum iriure dolor in hendrerit in vulputate velit esse molestie consequat, vel illum dolore eu feugiat nulla facilisis at vero eros et accumsan et iusto odio dignissim.</p>
    <p class="txt copy-small copy-b">Lorem ipsum dolor sit amet, consectetuer adipiscing elit, sed diam nonummy nibh euismod tincidunt ut laoreet dolore magna aliquam erat volutpat. Ut wisi enim ad minim veniam, quis nostrud exerci tation ullamcorper suscipit lobortis nisl ut aliquip ex ea commodo consequat. Duis autem vel eum iriure dolor in hendrerit.</p>
    <p class="txt copy-small copy-c">Lorem ipsum dolor sit amet, cons ectetuer adipiscing elit, sed diam nonummy nibh euismod tincidunt ut laoreet dolore magna aliquam erat volutpat. Ut wisi enim ad minim veniam, quis nostrud exerci tation ullamcorper suscipit lobortis nisl ut aliquip ex ea commodo consequat.</p>

    <ol class="txt steps">
      <li><span class="num">1</span><div><h3>Lorem ipsum</h3><p>Lorem ipsum dolor sit amet, consectetuer adipiscing elit, sed diam nonummy nibh euismod tincidunt ut</p></div></li>
      <li><span class="num">2</span><div><h3>Lorem ipsum</h3><p>Lorem ipsum dolor sit amet, consectetuer adipiscing elit, sed diam nonummy nibh euismod tincidunt ut</p></div></li>
      <li><span class="num">3</span><div><h3>Lorem ipsum</h3><p>Lorem ipsum dolor sit amet, consectetuer adipiscing elit, sed diam nonummy nibh euismod tincidunt ut</p></div></li>
      <li><span class="num">4</span><div><h3>Lorem ipsum</h3><p>Lorem ipsum dolor sit amet, consectetuer adipiscing elit, sed diam nonummy nibh euismod tincidunt ut</p></div></li>
      <li><span class="num">5</span><div><h3>Lorem ipsum</h3><p>Lorem ipsum dolor sit amet, consectetuer adipiscing elit, sed diam nonummy nibh euismod tincidunt ut</p></div></li>
    </ol>
  </section>

</div>
</body>
</html>
```